nutrition company business card

I would like to have a business card that has two sides, one being the green color from the Company name on the logo. I am open to ideas and looks that work with my logo. I like the idea of having a negative image of the tree on the green side.

For my information on the card I must have:
Linda Moorcombe
415-872-6041
lindamoorcombe@quellmail.net

This area will need to be updated once I complete my schooling.

Reason: I need to extend my deadline by one day as I have been sick the last week and not had time to review all the new designs. Thank you.

Industry/Entity Type

Nutrition

Requirements
Must have
• I would like to have a business card that has two sides, one being the green color from the Company name on the logo. I am open to ideas and looks that work with my logo. I like the idea of having a negative image of the tree on the green side.
• For my information on the card I must have:
• Linda Moorcombe
• 415-872-6041
• lindamoorcombe@quellmail.net
• This area will need to be updated once I complete my schooling.

```html
<!DOCTYPE html>
<html lang="en">
<head>
<meta charset="utf-8">
<title>Rooted Table – Business Card</title>
<link rel="stylesheet" href="https://fonts.googleapis.com/css2?family=Comfortaa:wght@400;600&display=swap">
<style>
  :root {
    --page-bg: #e8e6e2;
    --brand-green: #4cb82a;
    --brand-green-light: #7fd64a;
    --brand-green-deep: #2e9a1c;
    --bark: #7b6b64;
    --bark-dark: #5a4d48;
    --ink-grey: #6a6a6a;
    --paper: #ffffff;
  }
  * { box-sizing: border-box; margin: 0; padding: 0; }
  html, body {
    width: 1200px; height: 682px; overflow: hidden;
    background: var(--page-bg);
    font-family: "Comfortaa", "Quicksand", sans-serif;
  }
  .canvas { position: relative; width: 1200px; height: 682px; }

  .card {
    position: absolute;
    width: 540px; height: 309px;
    overflow: hidden;
    border-radius: 4px;
    box-shadow: 0 6px 18px rgba(0,0,0,.18);
  }
  .card-art { position: absolute; inset: 0; width: 100%; height: 100%; }

  /* Front side */
  .card--front { left: 40px; top: 186px; background: var(--paper); }
  .front__leaves {
    position: absolute; inset: 0;
    background:
      radial-gradient(ellipse 160px 110px at 250px 110px, rgba(255,255,255,.18), rgba(255,255,255,0) 70%),
      radial-gradient(ellipse 140px 90px at 70px 60px, rgba(255,255,255,.14), rgba(255,255,255,0) 70%);
  }
  .front__name {
    position: absolute; right: 28px; top: 28px;
    color: var(--paper); font-size: 22px; font-weight: 600;
  }
  .front__contact {
    position: absolute; right: 20px; top: 84px;
    display: flex; flex-direction: column; align-items: flex-end; gap: 8px;
    color: var(--paper); font-size: 12.5px; font-weight: 600;
  }
  .contact-line { display: flex; align-items: center; gap: 10px; }
  .contact-line svg { width: 18px; height: 14px; flex: none; }
  .front__brand { position: absolute; left: 208px; top: 230px; }
  .brand-name {
    color: var(--brand-green); font-size: 27px; font-weight: 400; line-height: 1;
  }
  .brand-tagline {
    color: var(--ink-grey); font-size: 15px; margin-top: 5px; letter-spacing: .5px;
  }

  /* Back side */
  .card--back {
    left: 620px; top: 186px;
    background: radial-gradient(ellipse at 35% 45%, var(--brand-green-light), var(--brand-green) 55%, var(--brand-green-deep));
  }
  .back__tree {
    position: absolute; inset: 0;
    background: linear-gradient(100deg, rgba(46,154,28,0) 45%, rgba(70,140,45,.45) 72%, rgba(90,77,72,.5) 100%);
  }
  .back__brand { position: absolute; left: 34px; top: 188px; }
  .back__brand .brand-name { color: var(--paper); font-size: 25px; }
  .back__brand .brand-tagline { color: var(--paper); font-size: 14px; }
</style>
</head>
<body>
<div class="canvas">

  <section class="card card--front">
    <svg class="card-art" viewBox="0 0 540 309" aria-hidden="true">
      <defs>
        <linearGradient id="frontGreen" x1="0" y1="0" x2="1" y2="1">
          <stop offset="0" stop-color="#7fd64a"/>
          <stop offset=".6" stop-color="#4cb82a"/>
          <stop offset="1" stop-color="#2e9a1c"/>
        </linearGradient>
      </defs>
      <path d="M0 0 H540 V160 Q300 185 0 262 Z" fill="url(#frontGreen)"/>
    </svg>
    <div class="front__leaves" role="img" aria-label="Faint leaf pattern across the green band"></div>
    <svg class="card-art" viewBox="0 0 540 309" aria-hidden="true">
      <path d="M0 262 Q300 185 540 160" fill="none" stroke="#7b6b64" stroke-width="3"/>
      <circle cx="110" cy="170" r="84" fill="#ffffff" stroke="#7b6b64" stroke-width="7"/>
    </svg>
    <div class="front__name">Linda Moorcombe</div>
    <div class="front__contact">
      <div class="contact-line">
        <span>415-872-6041</span>
        <svg viewBox="0 0 18 14" aria-hidden="true"><path d="M4 1 L7 4 L5.5 6 Q8 10 11 11 L13 9.5 L16 12.5 L14 14 Q6 13 2 4 Z" fill="#7b6b64"/></svg>
      </div>
      <div class="contact-line">
        <span>lindamoorcombe@quellmail.net</span>
        <svg viewBox="0 0 18 14" aria-hidden="true"><rect x="1" y="1.5" width="16" height="11" fill="none" stroke="#7b6b64" stroke-width="1.6"/><path d="M1 1.5 L9 8 L17 1.5" fill="none" stroke="#7b6b64" stroke-width="1.6"/></svg>
      </div>
    </div>
    <div class="front__brand">
      <div class="brand-name">Rooted Table</div>
      <div class="brand-tagline">simple food, happy homes</div>
    </div>
  </section>

  <section class="card card--back">
    <div class="back__tree" role="img" aria-label="Large negative tree illustration with heart in the trunk"></div>
    <svg class="card-art" viewBox="0 0 540 309" aria-hidden="true">
      <circle cx="150" cy="100" r="68" fill="#ffffff" stroke="#7b6b64" stroke-width="6"/>
    </svg>
    <div class="back__brand">
      <div class="brand-name">Rooted Table</div>
      <div class="brand-tagline">simple food, happy homes</div>
    </div>
  </section>

</div>
</body>
</html>
```